GDN Banners to promote Pop-ups Blocking security software

KVELT is software security company which develops products to fight different online threats such as scam offers, phishing web sites and spam. We believe that our solutions will help both non-technical and power users to browse Internet safely and avoid online threats.

With requested banners we would like to advertise one of the features of our product which allows users to block unwanted pop-ups at different media resources.
You can see demo of that feature at the landing page which will be used for banners: https://lps.kvelt-example.me/lp/popup-en/

1. Banners should catch the attention and be aligned with landing page.

2. Sizes: 120x600, 160x600, 300x600, 336x280, 300x250, 320x50, 468x60, 970x90. Most important size: 300x250

3. We use Open Sans font but need text in banners to support Vietnamese language.

4. Logo: same as web site https://lps.kvelt-example.me/lp/popup-en/

5.
Title - Never See Pop-UPs Again
Sub title - Enjoy Internet without Annoying and Unsafe Ads

6. CTA: Get Free
button should have same style as button at landing (color can be seen only in Brisa)

Target Market(s)

We target broad audience, who are concerned about online security. However this particular feature might be interesting for people who like to entertain online, watch video, listen to the music, etc. because usually there are a lot of pop-ups on such web sites. And most of such pop-ups are scam or malware.

Industry/Entity Type

Computer Security

Font styles to use
Sans Serif

Requirements
Must have
• Catchy visual element :) which provide good intuition about annoying / unwanted pop-up which can be removed forever by our product.

```html
<!DOCTYPE html>
<html lang="en">
<head>
<meta charset="utf-8">
<title>KVELT – Block Pop-Ups Banner</title>
<link rel="stylesheet" href="https://fonts.googleapis.com/css2?family=Open+Sans:wght@400;600;700&display=swap">
<style>
  :root {
    --panel: #3b4550;
    --teal: #63c5bb;
    --white: #ffffff;
    --muted: #dfe4ea;
    --button: #5a80d8;
    --stage-deep: #123f7a;
    --stage-light: #4fa9dc;
    --close-red: #e0393a;
    --bar-grey: #9aa0a6;
  }
  * { margin: 0; padding: 0; box-sizing: border-box; }
  html, body { width: 1200px; height: 2400px; overflow: hidden; background: var(--panel); }
  body { font-family: "Open Sans", Arial, sans-serif; color: var(--white); }

  .banner { position: relative; width: 1200px; height: 2400px; }

  .video {
    position: absolute; left: 0; top: 0; width: 1200px; height: 1048px;
    background: radial-gradient(ellipse at 55% 45%, var(--stage-light) 0%, #2b78bd 45%, var(--stage-deep) 100%);
    overflow: hidden;
  }
  .video-photo { position: absolute; inset: 0; }

  .popup-bar {
    position: absolute; left: 0; top: 164px; width: 564px; height: 60px;
  }
  .play-icon { position: absolute; left: 548px; top: 436px; width: 140px; height: 150px; }

  .panel { position: absolute; left: 0; top: 1048px; width: 1200px; height: 1352px; background: var(--panel); }

  .headline {
    position: absolute; top: 1120px; width: 100%; text-align: center;
    font-size: 118px; font-weight: 700; line-height: 1.1; letter-spacing: -1px;
  }
  .headline .accent { color: var(--teal); }

  .subhead {
    position: absolute; top: 1280px; width: 100%; text-align: center;
    font-size: 50px; font-weight: 400; color: var(--muted);
  }
  .subhead strong { font-weight: 700; color: var(--white); }

  .promise {
    position: absolute; top: 1592px; width: 100%; text-align: center;
    font-size: 86px; font-weight: 400; line-height: 1.3;
  }

  .cta {
    position: absolute; left: 232px; top: 2048px; width: 748px; height: 144px;
    background: var(--button); border-radius: 6px;
    display: flex; align-items: center; justify-content: center;
    font-size: 66px; font-weight: 600; letter-spacing: 2px; color: var(--white);
  }

  .brand {
    position: absolute; top: 2284px; left: 0; width: 100%;
    display: flex; align-items: center; justify-content: center; gap: 22px;
  }
  .brand-dot { width: 68px; height: 68px; border-radius: 50%; background: var(--teal); }
  .brand-name { font-size: 52px; font-weight: 700; color: var(--white); }
  .brand-tagline { font-size: 48px; font-weight: 600; color: var(--white); margin-left: 36px; }
</style>
</head>
<body>
<main class="banner">
  <section class="video">
    <div class="video-photo" role="img" aria-label="Fashion show runway scene on a blue-lit stage, playing as a video"></div>

    <svg class="popup-bar" viewBox="0 0 564 60" aria-hidden="true">
      <rect x="0" y="0" width="564" height="60" fill="#ffffff"/>
      <rect x="252" y="12" width="30" height="36" rx="3" fill="var(--bar-grey)"/>
      <circle cx="267" cy="24" r="6" fill="#ffffff"/>
      <rect x="320" y="32" width="24" height="4" fill="#555"/>
      <rect x="418" y="18" width="24" height="22" fill="none" stroke="#555" stroke-width="4"/>
      <rect x="484" y="0" width="80" height="60" fill="var(--close-red)"/>
      <path d="M510 16 L538 44 M538 16 L510 44" stroke="#ffffff" stroke-width="5"/>
    </svg>

    <svg class="play-icon" viewBox="0 0 140 150" aria-hidden="true">
      <polygon points="10,5 135,75 10,145" fill="#ffffff" fill-opacity="0.7"/>
    </svg>
  </section>

  <section class="panel"></section>

  <h1 class="headline">Block <span class="accent">Pop-Ups!</span></h1>
  <p class="subhead">Brisa <strong>Extension</strong> to <strong>Avoid Unsafe Ads</strong></p>

  <p class="promise">Watch Videos<br>without Distraction</p>

  <div class="cta">TRY NOW</div>

  <footer class="brand">
    <span class="brand-dot"></span>
    <span class="brand-name">KVELT</span>
    <span class="brand-tagline">Safe Browsing</span>
  </footer>
</main>
</body>
</html>
```